Launch Ledger: How to steer your early capital toward rapid expansion

I need a full-color book cover for a paperback (front, spine and back) in high resolution InDesign and PDF. I also need the derived version for an e-book. Here are some briefing elements:

Audience Profile
Imagine a person standing at the threshold of a significant milestone in their entrepreneurial journey, their heart a mix of excitement and anxiety. Having just secured Series A funding, they acknowledge the validation of their relentless effort and vision but are deeply conscious of the daunting challenges that lie ahead. This individual is navigating the complexities of rapid scaling, managing a larger and potentially more demanding board of directors, and restructuring the company's priorities while preserving its culture. The weight of expectations to succeed and propel the startup to new heights is palpable, stirring a sense of overwhelm amidst the triumph.

Reader Situation
The current state of our target reader might be a mix of excitement and anxiety. Having just secured Series A funding, they recognize the validation of their hard work and vision but are acutely aware of the mountain of challenges ahead. They may feel overwhelmed by the expectations to scale rapidly, manage a larger and potentially more demanding board of directors, and restructure the company's priorities while maintaining its culture. After reading this book and implementing its advice, they would feel empowered, equipped with a clear strategy for tackling the challenges that come with Series A funding, and confident in their ability to scale their startup efficiently. They will be on a promising path toward achieving growth targets necessary for a successful Series B raise, with a newfound understanding of how to manage their team and board dynamics effectively.
Updates

Got some good first attempts on the first round of submissions, I like many of the color schemes proposed and some people have submitted abstract pictures that chime really well with founders who are trying to grow the company.
Where many people fall short is in "Series A playbook" not being the most prominent title on the cover page, picking a picture that does not particularly chime with founders trying to reach higher growth for their company, and sometimes in just throwing some elements on a page and hoping something sticks :)
I'm actively reviewing 3 times per day so please try to follow the briefing and get to the top of the selection list.

Hello everybody, thank you for the designs coming in. There are some entries that are showing great potential! Some clarifications:

- "Series A" and by extension "Series A Playbook" should really be the most prominent part of the cover. If you split it up, make sure "Series A" is together on the same line as it is a term founders will (and must) recognize. If you use different sizes, make sure "Series A" is bigger than "Playbook"
- I much prefer the designs with simpler, more abstract pictures, eg an outline of a person is better than a detailed drawing of a person, but a drawing is still better than a photograph
- Some of you have been using very well known stock photos, we want this to be unique so those designs will not be favored.
- If you do have a person on the cover evoking a startup founder, then put them in clothes that people will recognize: typically a hoody, a tshirt with the logo of their startup, jeans or other comfortable pants, and sneakers. Do not put someone in a suit and tie.
- If you can, use the "footer bar" supplied at the bottom of the front cover to evoke our branding. You can just use the color bars, the logo can be somewhere else.
- The logo should be relatively small and we prefer it to be on the right (because of the arrow in the logo). It should be less prominent than the author name (Teodor Vasquell)
- Finally, I am starting to play closer attention to the spine and the back cover. Spine should be attractive and make it easy to find the book, with author name, title and the Crestway Academy logo (or just the icon). Back cover should have room for a summary, lots of testimonial quotes, a picture of the author and a bar code.

I will check designs daily and give feedback for every design submitted. Thank you all for putting in great work and I'm looking forward to picking a cover shortly!

Target Market(s)

Founders and employees of technology startups in North America, Europe and East Asia

Industry/Entity Type

Startups, technology, software

Font styles to use
Sans Serif

Requirements
Must have
• Dominant title, simple (conceptual) picture, look and feel of practical business book, attractive back cover inviting people to read quotes
Nice to have
• Picture on the front cover that evokes the feeling of having a guide, a map, a navigation tool, so that even if you don't know the exact road, you'll be all right. But ideally keep the picture more abstract and conceptual, I'm not looking for an elaborate illustration
Should not have
• Elaborate illustration, photo on the front cover, complex color scheme

```html
<!DOCTYPE html>
<html lang="en">
<head>
<meta charset="utf-8">
<title>Launch Ledger – Front Cover</title>
<link rel="stylesheet" href="https://fonts.googleapis.com/css2?family=Bebas+Neue&family=Barlow+Condensed:wght@500;700&display=swap">
<style>
  :root {
    --backdrop: #000000;
    --cover-yellow: #FFF200;
    --ink-navy: #1F2A37;
    --bar-green: #8FAE6B;
    --bar-teal: #3AA3B8;
    --bar-purple: #8B78AE;
    --bar-orange: #E39A2D;
    --bar-red: #E0572F;
  }
  html, body {
    margin: 0;
    padding: 0;
    width: 1200px;
    height: 1200px;
    overflow: hidden;
    background: var(--backdrop);
  }
  .cover-art {
    display: block;
    width: 1200px;
    height: 1200px;
  }
  .cover-face { fill: var(--cover-yellow); }
  .title-line {
    font-family: "Bebas Neue", "Oswald", sans-serif;
    font-size: 224px;
    fill: var(--ink-navy);
  }
  .subtitle {
    font-family: "Barlow Condensed", "Arial Narrow", sans-serif;
    font-size: 33px;
    letter-spacing: 2.5px;
    fill: var(--ink-navy);
    text-anchor: middle;
  }
  .subtitle--light { font-weight: 500; }
  .subtitle--bold { font-weight: 700; }
  .publisher-name {
    font-family: "Barlow Condensed", "Arial Narrow", sans-serif;
    font-weight: 500;
    font-size: 19px;
    letter-spacing: 1.5px;
    fill: var(--ink-navy);
    text-anchor: middle;
  }
  .publisher-square {
    fill: none;
    stroke: var(--ink-navy);
    stroke-width: 4;
  }
</style>
</head>
<body>
<svg class="cover-art" viewBox="0 0 1458 1458" xmlns="http://www.w3.org/2000/svg" aria-label="Launch Ledger front cover">
  <defs>
    <linearGradient id="emblem-tones" x1="0" y1="0" x2="1" y2="0">
      <stop offset="0" stop-color="var(--bar-purple)"/>
      <stop offset="0.35" stop-color="var(--bar-teal)"/>
      <stop offset="0.65" stop-color="var(--bar-orange)"/>
      <stop offset="1" stop-color="var(--bar-red)"/>
    </linearGradient>
  </defs>

  <!-- Cover panel -->
  <rect class="cover-face" x="379" y="204" width="701" height="1050"/>

  <!-- Brand colour bar, top -->
  <g class="brand-bar brand-bar--top">
    <rect x="379" y="204" width="117" height="14" fill="var(--bar-green)"/>
    <rect x="496" y="204" width="293" height="14" fill="var(--bar-teal)"/>
    <rect x="789" y="204" width="291" height="14" fill="var(--bar-purple)"/>
  </g>

  <!-- Emblem area -->
  <rect class="growth-emblem" x="606" y="245" width="250" height="165" rx="10"
        fill="url(#emblem-tones)" opacity="0.85"
        role="img" aria-label="Colourful growth chart emblem with a rising arrow"/>

  <!-- Publisher name -->
  <g class="publisher">
    <rect class="publisher-square" x="969" y="272" width="36" height="36"/>
    <text class="publisher-name" x="987" y="334">CRESTWAY</text>
    <text class="publisher-name" x="987" y="354">ACADEMY</text>
  </g>

  <!-- Title -->
  <g class="title">
    <text class="title-line" transform="translate(450 578) scale(1 0.93)" textLength="557" lengthAdjust="spacingAndGlyphs">LAUNCH</text>
    <text class="title-line" transform="translate(450 1108) scale(1 3.18)" textLength="557" lengthAdjust="spacingAndGlyphs">LEDGER</text>
  </g>

  <!-- Subtitle -->
  <text class="subtitle subtitle--light" x="729" y="1165">HOW TO STEER YOUR EARLY CAPITAL</text>
  <text class="subtitle subtitle--bold" x="729" y="1203">TOWARD RAPID EXPANSION</text>

  <!-- Brand colour bar, bottom -->
  <g class="brand-bar brand-bar--bottom">
    <rect x="379" y="1240" width="117" height="14" fill="var(--bar-green)"/>
    <rect x="496" y="1240" width="293" height="14" fill="var(--bar-orange)"/>
    <rect x="789" y="1240" width="291" height="14" fill="var(--bar-red)"/>
  </g>
</svg>
</body>
</html>
```